Start-up Dog Daycare Needs a Retractable Banner Design for Career Fair

We are a dog daycare located in San Francisco, California, called TailNest Dog Daycare. Our small but dog-knowledgeable team gets to interact with and care for dogs on a daily basis where we supervise playgroups of various sizes. We will like a modern yet fun banner to attract potential new hires and interns. We will like the final design to communicate that we are seeking people who love dogs but who are also hard workers that can thrive in a team setting.

The product specs are as follows:
Document Trim Size - 33.13 X 86.18 inches (84.1 X 218.9cm) with 3312 X 8618 pixels.
Full Bleed Size - 33.38 X 86.43 inches (84.8 X 219.5cm) with 3338 X 8643 pixels.

Additionally, to get a better idea of our brand, attached will be our Company Brand Identity.
Furthermore, attached will be the text we will like included onto our banner.

Target Market(s)

Students at a University

Industry/Entity Type

Pet Care

Font styles to use
Sans Serif

Colors
33a6d7
fbee3e

Requirements
Must have
• Our company logo must be incorporated onto our banner.
• Please include the text in the following order:
• 1. "Dog lovers come talk to us"
• 2. "Internships and full-time positions available"
• Banner Size Specifications:
• Full Bleed Size
• 33.38" x 86.43"
• 84.8 x 219.5 cm
• 3338 x 8643 pixels
• Document Trim Size
• 33.13" x 86.18"
• 84.1 x 218.9 cm
• 3312 x 8618 pixels
• Finished artwork should extend to fill the full bleed area to avoid white edges around.
Nice to have
• - Colors Blue and Yellow
• - Image(s) of a dog(s) playing

```html
<!DOCTYPE html>
<html lang="en">
<head>
<meta charset="utf-8">
<title>TailNest Dog Daycare – Career Fair Banner</title>
<link rel="stylesheet" href="https://fonts.googleapis.com/css2?family=Fredoka:wght@500;600;700&family=Montserrat:wght@600&display=swap">
<style>
  :root {
    --brand-blue: #33a6d7;
    --brand-yellow: #fbee3e;
    --ink: #0d0d0d;
    --dog-grey: #dcd9d4;
  }
  * { margin: 0; padding: 0; box-sizing: border-box; }
  html, body {
    width: 720px;
    height: 1200px;
    overflow: hidden;
    background: #ffffff;
  }
  .banner {
    position: relative;
    width: 720px;
    height: 1200px;
    background: var(--brand-blue);
    overflow: hidden;
    font-family: "Fredoka", sans-serif;
    color: var(--ink);
    text-align: center;
  }
  .ground-band {
    position: absolute;
    inset: 0;
    width: 720px;
    height: 1200px;
  }
  .brand-marker {
    position: absolute;
    top: 62px;
    left: 305px;
    width: 110px;
    height: 110px;
    border-radius: 50%;
    background: var(--dog-grey);
  }
  .brand-name {
    position: absolute;
    top: 204px;
    left: 0;
    width: 100%;
    font-weight: 600;
    font-size: 90px;
    line-height: 1;
    color: var(--brand-yellow);
    letter-spacing: 1px;
  }
  .brand-tagline {
    position: absolute;
    top: 308px;
    left: 0;
    width: 100%;
    font-family: "Montserrat", sans-serif;
    font-weight: 600;
    font-size: 22px;
    line-height: 1;
    letter-spacing: 5px;
  }
  .headline {
    font-weight: 700;
    text-transform: uppercase;
    line-height: 1;
  }
  .headline span {
    position: absolute;
    left: 0;
    width: 100%;
    display: block;
  }
  .headline-top { top: 378px; font-size: 72px; }
  .headline-accent {
    top: 436px;
    font-size: 134px;
    color: var(--brand-yellow);
    -webkit-text-stroke: 3px var(--ink);
    paint-order: stroke fill;
    letter-spacing: 2px;
  }
  .headline-bottom { top: 550px; font-size: 72px; }
  .dog-illustration {
    position: absolute;
    left: 20px;
    top: 790px;
    width: 680px;
    height: 230px;
  }
  .positions {
    position: absolute;
    top: 638px;
    left: 0;
    width: 100%;
    font-weight: 600;
    font-size: 42px;
    line-height: 48px;
  }
  .contact-label {
    position: absolute;
    top: 1036px;
    left: 0;
    width: 100%;
    font-weight: 600;
    font-size: 24px;
    line-height: 1;
  }
  .contact-url {
    position: absolute;
    top: 1080px;
    left: 0;
    width: 100%;
    font-weight: 700;
    font-size: 38px;
    line-height: 1;
  }
</style>
</head>
<body>
  <main class="banner">
    <svg class="ground-band" viewBox="0 0 720 1200" aria-hidden="true">
      <polygon points="0,843 720,1010 720,1200 0,1200" fill="var(--brand-yellow)"/>
    </svg>

    <div class="brand-marker" aria-hidden="true"></div>
    <div class="brand-name">TailNest</div>
    <div class="brand-tagline">DOG DAYCARE</div>

    <h1 class="headline">
      <span class="headline-top">Dog Lovers</span>
      <span class="headline-accent">Come</span>
      <span class="headline-bottom">Talk to Us!</span>
    </h1>

    <svg class="dog-illustration" viewBox="0 0 680 230" role="img" aria-label="Large line illustration of a dog in a play bow pose">
      <rect x="0" y="0" width="680" height="230" rx="115" fill="var(--dog-grey)"/>
    </svg>

    <p class="positions">Internships and<br>Full-time Positions<br>Available!</p>

    <div class="contact-label">For More Information</div>
    <div class="contact-url">www.TailNestDogs.com</div>
  </main>
</body>
</html>
```